QZN Supplements needs a label designer for supplement company

Looking for an on going label designer for my supplement company. I have three products that will need designs. I'm about to launch my sleep supplement called Velmora Rest and that's the first design needed.
I would like all designs to be somewhat simple, not overstated and uniformed so that when you look at all of the labels of the different supplements they are similar and you can tell it's the same brand.
Please see attached sample pictures below as ideas.
Updates

The brand is QZN supplements, logo file has been provided. The supplement is called Velmora Rest. It is a liquid supplement that is a 32/33 ounce white bottle. Die lines and measurements will be provided. Here's text for wording ideas: Wording: Natural Sleep Aid Reset your circadian rhythm. May help you: Fall asleep faster. Get a deeper more restful sleep. Boost Immune System Remember your dreams. Protect your brain and flush toxins. Wake up feeling refreshed. Non-gmo Gluten Free Sugar Free Vegan Manufactured in cGMP factory Manufactured in USA

Target Market(s)

Health and wellness/supplement industry for regular people not hardcore gym goers. My supplements are for a health lifestyle not bodybuilding.

Industry/Entity Type

Health And Wellness

Colors
3176b5
3276b5
33a6d7
85cae6
85abd2
cedeed
e4daeb
b7a5cd

Requirements
Must have
• There will be some text and wording that I will provide that must be on the bottles.

```html
<!DOCTYPE html>
<html lang="en">
<head>
<meta charset="utf-8">
<title>QZN Supplements – Velmora Rest Label Variants</title>
<link rel="stylesheet" href="https://fonts.googleapis.com/css2?family=Montserrat:wght@200;300;400;700;800&family=Oswald:wght@500;600&family=Barlow+Condensed:wght@500&display=swap">
<style>
  :root {
    --canvas-bg: #8a8a8a;
    --label-white: #ffffff;
    --label-purple: #b3a0cb;
    --label-purple-deep: #a08bbd;
    --brand-ink: #1a1d2e;
    --accent-green: #1ff01f;
    --text-light: #ffffff;
    --halo: rgba(255,255,255,0.55);
  }
  * { margin: 0; padding: 0; box-sizing: border-box; }
  html, body { width: 1200px; height: 1140px; overflow: hidden; }
  body {
    background: var(--canvas-bg);
    display: flex;
    align-items: center;
    justify-content: center;
    gap: 45px;
    font-family: "Montserrat", sans-serif;
  }
  .label {
    width: 340px;
    height: 960px;
    background: var(--label-purple);
    border-radius: 14px;
    overflow: hidden;
    display: flex;
    flex-direction: column;
    align-items: center;
    box-shadow: 0 6px 18px rgba(0,0,0,0.25);
  }
  .label__brand-band {
    width: 100%;
    height: 190px;
    background: var(--label-white);
    border-bottom-left-radius: 50% 30px;
    border-bottom-right-radius: 50% 30px;
    display: flex;
    align-items: center;
    justify-content: center;
    gap: 12px;
    padding-top: 40px;
  }
  .brand-mark {
    width: 46px;
    height: 46px;
    border-radius: 50%;
    background: var(--brand-ink);
    flex-shrink: 0;
  }
  .brand-name {
    font-family: "Oswald", sans-serif;
    font-weight: 600;
    font-size: 30px;
    letter-spacing: 0.5px;
    color: var(--brand-ink);
    text-transform: uppercase;
  }
  .product-title {
    margin-top: 62px;
    text-align: center;
    color: var(--text-light);
    line-height: 1;
  }
  .product-title__light {
    display: block;
    font-weight: 200;
    font-size: 44px;
    letter-spacing: 1px;
  }
  .product-title__bold {
    display: block;
    font-weight: 700;
    font-size: 56px;
    margin-top: 4px;
  }
  .product-subtitle {
    margin-top: 10px;
    font-weight: 300;
    font-size: 15px;
    color: var(--text-light);
    letter-spacing: 0.3px;
  }
  .label--green-title .product-title { color: var(--accent-green); }
  .sleep-art {
    margin-top: 40px;
    width: 230px;
    height: 230px;
    border-radius: 50%;
    background: radial-gradient(circle, #c2b3d6 0%, #b8a7d0 45%, var(--halo) 62%, var(--label-purple) 72%);
  }
  .benefits {
    margin-top: 40px;
    text-align: center;
    color: var(--accent-green);
    font-weight: 300;
    font-size: 21px;
    line-height: 1.3;
  }
  .benefits strong { font-weight: 800; }
  .net-weight {
    margin-top: 42px;
    font-family: "Barlow Condensed", sans-serif;
    font-weight: 500;
    font-size: 18px;
    color: var(--text-light);
  }
</style>
</head>
<body>
  <section class="label">
    <header class="label__brand-band">
      <span class="brand-mark"></span>
      <span class="brand-name">QZN Supplements</span>
    </header>
    <h1 class="product-title">
      <span class="product-title__light">VELMORA</span>
      <span class="product-title__bold">REST</span>
    </h1>
    <p class="product-subtitle">NATURAL SLEEP AID</p>
    <div class="sleep-art" role="img" aria-label="Line illustration of a brain with a multicolour moon, cloud and Z sleep icons inside a dotted halo"></div>
    <p class="benefits">Fall Asleep <strong>Faster</strong><br>Stay Asleep <strong>Longer</strong></p>
    <p class="net-weight">Net Wt. 2 LBs (32oz)</p>
  </section>

  <section class="label label--green-title">
    <header class="label__brand-band">
      <span class="brand-mark"></span>
      <span class="brand-name">QZN Supplements</span>
    </header>
    <h1 class="product-title">
      <span class="product-title__light">VELMORA</span>
      <span class="product-title__bold">REST</span>
    </h1>
    <p class="product-subtitle">NATURAL SLEEP AID</p>
    <div class="sleep-art" role="img" aria-label="Line illustration of a brain with green moon, cloud and Z sleep icons inside a dotted halo"></div>
    <p class="benefits">Fall Asleep <strong>Faster</strong><br>Stay Asleep <strong>Longer</strong></p>
    <p class="net-weight">Net Wt. 2 LBs (32oz)</p>
  </section>

  <section class="label">
    <header class="label__brand-band">
      <span class="brand-mark"></span>
      <span class="brand-name">QZN Supplements</span>
    </header>
    <h1 class="product-title">
      <span class="product-title__light">VELMORA</span>
      <span class="product-title__bold">REST</span>
    </h1>
    <p class="product-subtitle">NATURAL SLEEP AID</p>
    <div class="sleep-art" role="img" aria-label="Line illustration of a brain with green moon, cloud and Z sleep icons inside a dotted halo"></div>
    <p class="benefits">Fall Asleep <strong>Faster</strong><br>Stay Asleep <strong>Longer</strong></p>
    <p class="net-weight">Net Wt. 2 LBs (32oz)</p>
  </section>
</body>
</html>
```